Life Coach for Lawyers Business Card Design

Elegant, original, business card design for life coaching service for associate attorneys who work in big law and struggle with stress, overwhelm, and time management. Double sided design.

Target Market(s)

Women associate attorneys who work in big law and struggle with stress, overwhelm, and time management.

Industry/Entity Type

Life Coaching

Contact Information for Business Card

Marissa Pendrell
Life Coach
518.677.3941
calmbriefcounsel.net
marissa@calmbriefcounsel.net
@calmbriefcounsel (Instagram)

Font styles to use
Other font styles liked:
• Silver South font duo. See uploaded files.

Requirements
Must have
• Icons for phone, website, email, and Instagram instead of words. Specific colors used in my logo (171B2B, 421121, FFFFFF)
Nice to have
• Foil. Embossed. Feminine design.
Should not have
• Any colors other than those used in logo. See uploaded files.

```html
<!DOCTYPE html>
<html lang="en">
<head>
<meta charset="utf-8">
<title>Marissa Pendrell – Life Coach Business Card</title>
<link rel="stylesheet" href="https://fonts.googleapis.com/css2?family=Cinzel:wght@400;700&family=Great+Vibes&display=swap">
<style>
  :root {
    --page: #d6d7d9;
    --card: #ffffff;
    --plum: #421121;
    --ink: #171b2b;
    --rose: #8a4a55;
    --blush: #f6e1e5;
    --seal: #f5d9de;
  }
  * { margin: 0; padding: 0; box-sizing: border-box; }
  html, body { width: 1200px; height: 1000px; overflow: hidden; }
  body { background: var(--page); position: relative; font-family: "Cinzel", serif; }

  .card {
    position: absolute;
    left: 265px;
    width: 670px;
    height: 383px;
    background: var(--card);
    overflow: hidden;
  }
  .card--front { top: 78px; }
  .card--back { top: 539px; }

  /* Front */
  .brush-stroke {
    position: absolute;
    left: 80px; top: 135px;
    width: 510px; height: 117px;
    background: linear-gradient(100deg, rgba(246,225,229,0.6) 0%, var(--blush) 12%, var(--blush) 88%, rgba(246,225,229,0.5) 100%);
    border-radius: 40px 10px 50px 12px;
    transform: rotate(-2deg);
  }
  .front-name {
    position: absolute;
    left: 0; right: 0; top: 150px;
    text-align: center;
    font-family: "Great Vibes", cursive;
    font-size: 62px;
    color: var(--rose);
    line-height: 1;
  }
  .front-title {
    position: absolute;
    left: 0; right: 0; top: 214px;
    text-align: center;
    font-size: 14px;
    letter-spacing: 3px;
    color: var(--plum);
  }

  /* Back */
  .seal {
    position: absolute;
    left: 182px; top: 24px;
    width: 340px; height: 340px;
  }
  .back-details {
    position: absolute;
    left: 0; right: 0; top: 93px;
    text-align: center;
    color: var(--plum);
  }
  .back-name {
    font-size: 22px;
    font-weight: 700;
    letter-spacing: 4.5px;
    line-height: 1;
  }
  .back-title {
    margin-top: 13px;
    font-size: 17px;
    font-weight: 700;
    letter-spacing: 3px;
    line-height: 1;
  }
  .contact-list { list-style: none; margin-top: 22px; color: var(--ink); }
  .contact-list li {
    font-size: 12px;
    letter-spacing: 2px;
    line-height: 1;
    margin-bottom: 20px;
  }
</style>
</head>
<body>
  <section class="card card--front">
    <div class="brush-stroke" role="img" aria-label="Soft blush pink painted brush stroke behind the name"></div>
    <div class="front-name">Marissa Pendrell</div>
    <div class="front-title">LIFE COACH</div>
  </section>

  <section class="card card--back">
    <svg class="seal" viewBox="0 0 340 340" aria-hidden="true">
      <circle cx="170" cy="170" r="165" fill="none" stroke="var(--seal)" stroke-width="2"/>
      <text x="170" y="178" text-anchor="middle" font-family="Cinzel, serif" font-size="22" letter-spacing="4" fill="var(--seal)">CALM BRIEF COUNSEL</text>
    </svg>
    <div class="back-details">
      <h1 class="back-name">MARISSA PENDRELL</h1>
      <p class="back-title">LIFE COACH</p>
      <ul class="contact-list">
        <li>518.677.3941</li>
        <li>CALMBRIEFCOUNSEL.NET</li>
        <li>MARISSA@CALMBRIEFCOUNSEL.NET</li>
        <li>@CALMBRIEFCOUNSEL (INSTAGRAM)</li>
      </ul>
    </div>
  </section>
</body>
</html>
```